Help our Crumb Parlour find our winning design! We're looking for a business card....

We’re a Crumb Parlour in NY specializing in custom-made cakes and unique desserts.
Our cakes combine flavor and art, each designed to match customer’s special event and theme.
We’d like a unique business card with a clean design that will combine French chic and artistic look & feel.
We’d like to differentiate ourselves from standard bakeries, please don’t offer cupcake images :-)
Our logo is peach-pink and brown and we’d love to use these colors ( . Another color that can be added is gold - or feel free to suggest!

Target Market(s)

Women, ages 25-55

Industry/Entity Type

Boutique

Contact Information for Business Card

Text on card:
Logo
Crumb Parlour by Dana Whitfield

www.xxxxxxxx.com
xxx@xxxxx.com
(516) xxx-xxxx
F – xxxxxxxxxx
IG - xxxxxxxxx

Font styles to use
Sans Serif
Script

Requirements
Must have
• Logo
• Clean look
• French chic and artistic look & feel.
Nice to have
• Damask pattern
Should not have
• Cupcake images

```html
<!DOCTYPE html>
<html lang="en">
<head>
<meta charset="utf-8">
<title>Crumb Parlour – Business Card</title>
<link rel="stylesheet" href="https://fonts.googleapis.com/css2?family=Play:wght@400;700&display=swap">
<style>
  :root {
    --page: #e9e7e4;
    --card: #ffffff;
    --pink: #f08aa3;
    --pink-soft: #f6b3c4;
    --grey: #6d6966;
    --ink: #3a3a3a;
  }
  * { margin: 0; padding: 0; box-sizing: border-box; }
  html, body {
    width: 1200px; height: 901px; overflow: hidden;
    background: var(--page);
    font-family: "Play", "Segoe UI", sans-serif;
  }
  .card {
    position: absolute; left: 100px; top: 170px;
    width: 1000px; height: 560px;
    background: var(--card);
    border-radius: 56px;
    overflow: hidden;
    box-shadow: 0 18px 40px rgba(0,0,0,.18);
  }
  .card__swoosh { position: absolute; inset: 0; width: 100%; height: 100%; }
  .brand {
    position: absolute; left: 60px; top: 150px; width: 370px;
    display: flex; align-items: center; justify-content: center; gap: 14px;
  }
  .brand__dot { width: 16px; height: 16px; border-radius: 50%; background: var(--pink); flex: none; }
  .brand__name { font-size: 40px; font-weight: 400; color: var(--grey); letter-spacing: 1px; white-space: nowrap; }
  .divider {
    position: absolute; left: 470px; top: 90px;
    width: 2px; height: 300px; background: var(--pink);
  }
  .contact-block { position: absolute; left: 505px; top: 88px; }
  .person__name { font-size: 36px; font-weight: 400; color: var(--pink); letter-spacing: 1.5px; }
  .person__title { font-size: 17px; font-weight: 700; color: var(--ink); letter-spacing: 1px; text-transform: uppercase; margin-top: 2px; }
  .contact-list { list-style: none; margin-top: 56px; }
  .contact-list li {
    display: flex; align-items: center; gap: 14px;
    font-size: 20px; color: var(--ink); letter-spacing: 1px;
    height: 34px;
  }
  .contact-list svg { width: 20px; height: 20px; flex: none; fill: var(--pink); }
</style>
</head>
<body>
  <main class="card">
    <svg class="card__swoosh" viewBox="0 0 1000 560" aria-hidden="true">
      <path d="M0 330 C 260 420, 620 470, 1000 520 L1000 560 L0 560 Z" fill="var(--pink)"/>
      <path d="M0 345 C 260 435, 620 485, 1000 535 L1000 560 L0 560 Z" fill="#fff"/>
      <path d="M0 360 C 260 450, 620 500, 1000 548 L1000 560 L0 560 Z" fill="var(--grey)"/>
    </svg>

    <div class="brand">
      <span class="brand__dot"></span>
      <span class="brand__name">Crumb Parlour</span>
    </div>

    <div class="divider"></div>

    <section class="contact-block">
      <h1 class="person__name">Dana Whitfield</h1>
      <p class="person__title">Managing Director</p>
      <ul class="contact-list">
        <li>
          <svg viewBox="0 0 24 24"><path d="M6.6 10.8a15 15 0 0 0 6.6 6.6l2.2-2.2c.3-.3.7-.4 1-.2 1.1.4 2.3.6 3.6.6.6 0 1 .4 1 1V20c0 .6-.4 1-1 1C10.6 21 3 13.4 3 4c0-.6.4-1 1-1h3.5c.6 0 1 .4 1 1 0 1.3.2 2.5.6 3.6.1.3 0 .7-.2 1z"/></svg>
          (516) 555 0142
        </li>
        <li>
          <svg viewBox="0 0 24 24"><path d="M7 1h10a2 2 0 0 1 2 2v18a2 2 0 0 1-2 2H7a2 2 0 0 1-2-2V3a2 2 0 0 1 2-2zm0 3v14h10V4zm5 15.5a1 1 0 1 0 0 2 1 1 0 0 0 0-2z"/></svg>
          (516) 555 0143
        </li>
        <li>
          <svg viewBox="0 0 24 24"><path d="M6 2h9l3 3v5H6zM3 11h18v8h-3v3H6v-3H3zm5 5v4h8v-4z"/></svg>
          (516) 555 0144
        </li>
        <li>
          <svg viewBox="0 0 24 24"><path d="M2 5h20v14H2zm2 2v.4l8 5.3 8-5.3V7zm0 2.8V17h16V9.8l-8 5.3z"/></svg>
          hello@crumbparlour.com
        </li>
        <li>
          <svg viewBox="0 0 24 24"><path d="M12 2a10 10 0 1 0 0 20 10 10 0 0 0 0-20zm6.9 6h-3a15 15 0 0 0-1.3-3.9A8 8 0 0 1 18.9 8zM12 4c.8 1.2 1.5 2.5 1.9 4h-3.8c.4-1.5 1.1-2.8 1.9-4zM4.3 14a8 8 0 0 1 0-4h3.4a16 16 0 0 0 0 4zm.8 2h3a15 15 0 0 0 1.3 3.9A8 8 0 0 1 5.1 16zm3-8h-3a8 8 0 0 1 4.3-3.9C8.8 5.3 8.4 6.6 8.1 8zM12 20c-.8-1.2-1.5-2.5-1.9-4h3.8c-.4 1.5-1.1 2.8-1.9 4zm2.3-6H9.7a14 14 0 0 1 0-4h4.6a14 14 0 0 1 0 4zm.3 5.9c.6-1.2 1-2.5 1.3-3.9h3a8 8 0 0 1-4.3 3.9zm1.7-5.9a16 16 0 0 0 0-4h3.4a8 8 0 0 1 0 4z"/></svg>
          www.crumbparlour-ny.com
        </li>
      </ul>
    </section>
  </main>
</body>
</html>
```